Petal Sprite - web design for my new flower atelier

I would like to ask for design proposal for my newly established flower atelier. My brand name is Petal Sprite and I focus on realisation of events and flower projects (any kind) for physical as well as legel persons. I don’t operate as a standard flowershop. I would like to have 5 key parts - 1/Landing pg/welcome, 2/About me, 3/Gallery, 4/References, 5/Contact details. I would like the web design to reflect the way I am/ I do the things, ie, be slightly different, do non-tradiotional arrangements, my passion for flowers, gentle& fregile style, love for minimalism and details in the arrangements. I attach couple of photos of what I do so that you can better understand my style . You can see more on IG mirka_petal_sprite or FB Petal Sprite. I was wondering maybe one of the first 2 photos could be part of the landing pg. Or another idea is to have a design similar to this one https://thistlebloomstudio.example, ie to choose 3-5photos which are being animated like here. However, I am open to discuss any ideas and look forward for all the proposals.

Target Market(s)

physical as well as legal persons - weddings, celebrations, business events, projects for hotels, beaty salons, restaurants and others.. actually any kind of flower project

Industry/Entity Type

flowers

Number of Pages Required

1 page

Font styles to use
Other font styles liked:
• the font which matches the logo font style

Requirements
Must have
• to reflect the way I am as described above, I prefer more simple way of design, with the attention to a detail, I prefer pastel colours

```html
<!DOCTYPE html>
<html lang="en">
<head>
<meta charset="utf-8">
<title>Petal Sprite</title>
<link href="https://fonts.googleapis.com/css2?family=Poppins:wght@400;500;600;700;800&display=swap" rel="stylesheet">
<style>
:root{
  --pink:#e4518b;
  --pink-soft:#f8dbe3;
  --pink-band:#fdedf2;
  --ink:#111111;
  --grey:#5b5b5b;
  --muted:#8a8a8a;
  --white:#ffffff;
}
*{margin:0;padding:0;box-sizing:border-box}
html,body{width:1200px;height:3421px;overflow:hidden;background:var(--white)}
body{position:relative;font-family:'Poppins',sans-serif;color:var(--ink)}
.abs{position:absolute}
.topbar{left:0;top:0;width:1200px;height:36px;background:#fbe9ee}
.topbar .info{top:12px;font-size:9px;font-weight:600}
.topbar .info span{color:var(--pink);font-weight:500}
.social{top:0;width:26px;height:36px}
.account{top:12px;font-size:9px;color:var(--pink);display:flex;align-items:center;gap:5px}
.nav{left:0;top:36px;width:1200px;height:50px;background:var(--white);box-shadow:0 3px 8px rgba(0,0,0,.08);z-index:2}
.logo{left:141px;top:10px;font-size:22px;font-weight:700;color:var(--pink)}
.nav a{position:absolute;top:17px;font-size:12px;font-weight:600;color:var(--pink);text-decoration:none;transform:translateX(-50%)}
.login-btn{left:920px;top:14px;width:71px;height:20px;border-radius:10px;background:var(--pink);color:#fff;font-size:8px;font-weight:600;display:flex;align-items:center;justify-content:center}
.hero{left:0;top:86px;width:1200px;height:458px;background:var(--pink-soft)}
.hero h1{left:142px;top:140px;font-size:58px;font-weight:700;letter-spacing:-.5px}
.hero h2{left:142px;top:218px;font-size:23px;font-weight:500;color:var(--pink)}
.hero p{left:142px;top:260px;width:330px;font-size:9.5px;line-height:20px;color:var(--grey)}
.work-btn{left:138px;top:333px;width:111px;height:32px;border-radius:16px;background:var(--ink);color:#fff;font-size:11px;font-weight:600;display:flex;align-items:center;justify-content:center}
.hero-visual{left:610px;top:0;width:505px;height:458px;background:radial-gradient(ellipse at 55% 45%,#f6c3d2 0%,#f1c9d4 35%,#f8dce3 75%)}
.why{left:126px;top:555px;width:948px;height:464px;background:var(--pink-soft)}
.video{left:-1px;top:46px;width:439px;height:275px;background:linear-gradient(160deg,#8b7a3a,#b59a2c 45%,#5c5a26);overflow:hidden}
.video .bar{left:0;bottom:32px;width:100%;height:2px;background:rgba(255,255,255,.35)}
.video .bar i{position:absolute;left:0;top:0;width:88%;height:2px;background:#4a8fd8}
.video .ctrl{left:0;bottom:0;width:100%;height:32px;background:rgba(0,0,0,.35)}
.why h3{left:488px;top:48px;font-size:40px;font-weight:700}
.why h3 span{color:var(--pink)}
.why .copy{left:488px;top:118px;width:455px;font-size:8.5px;line-height:20px;color:var(--grey)}
.feature{top:357px;width:230px;height:82px;background:#fff;display:flex;align-items:center;gap:12px;padding-left:32px}
.feature b{display:block;font-size:13px;font-weight:600;line-height:16px}
.feature small{display:block;font-size:10.5px;line-height:14px}
.band{height:56px;background:var(--pink-band);display:flex;align-items:center;justify-content:center;font-size:29px;font-weight:700}
.band span{color:var(--pink)}
.card{width:300px;height:305px;background:#fff;box-shadow:0 1px 5px rgba(0,0,0,.18)}
.card .tag{left:12px;top:14px;font-size:13px;font-weight:700;color:var(--pink)}
.card .pic{left:60px;top:14px;width:180px;height:210px;border-radius:40% 40% 30% 30%}
.card .name{left:0;top:226px;width:100%;text-align:center;font-size:26px;font-weight:500;color:var(--grey)}
.card .event{left:0;top:259px;width:100%;text-align:center;font-size:22px;font-weight:700;color:var(--pink)}
.card .event small{font-size:11px;color:var(--muted);font-weight:600}
.review{top:2159px;width:292px;height:337px;background:#fff;box-shadow:0 1px 6px rgba(0,0,0,.15);border-radius:4px}
.stars{left:22px;top:58px}
.review p{left:22px;top:98px;width:250px;font-size:9.6px;line-height:20px;font-weight:600;color:var(--grey)}
.avatar{left:22px;top:230px;width:60px;height:60px;border-radius:50%}
.review .who{left:90px;top:238px}
.review .who b{display:block;font-size:20px;font-weight:700;line-height:24px}
.review .who small{display:block;font-size:10px;color:var(--muted)}
.form{left:129px;top:2612px;width:471px;height:400px;background:#fff;box-shadow:0 1px 6px rgba(0,0,0,.12)}
.field{left:21px;width:429px;height:43px;border:1.5px solid #ef9fbf;border-radius:4px;font-size:17px;padding:10px 24px;color:var(--ink)}
.illus{left:644px;top:2647px;width:351px;height:339px;border-radius:45%;background:radial-gradient(circle at 50% 55%,#f6d0de,#f3f3f3 60%,#fff 80%)}
.foot h4{top:3042px;font-size:29px;font-weight:600;color:#4a4a4a}
.foot a{position:absolute;font-size:17px;color:var(--grey);text-decoration:none;white-space:nowrap}
</style>
</head>
<body>

<header class="abs topbar">
  <div class="abs info" style="left:179px">Phone No: <span>555 014 2290</span></div>
  <div class="abs info" style="left:324px">Email ID: <span>studio@petalsprite.example</span></div>
  <div class="abs social" style="left:763px;background:#e4518b"></div>
  <div class="abs social" style="left:790px;background:#ec7aa6"></div>
  <div class="abs social" style="left:817px;background:#d6406f"></div>
  <div class="abs social" style="left:844px;background:#f09ab9"></div>
  <div class="abs account" style="left:906px">
    <svg width="10" height="11" viewBox="0 0 10 11"><rect x="1" y="5" width="8" height="6" rx="1" fill="#111"/><path d="M3 5V3a2 2 0 0 1 4 0v2" stroke="#111" fill="none" stroke-width="1.4"/></svg>Login</div>
  <div class="abs account" style="left:970px">
    <svg width="10" height="11" viewBox="0 0 10 11"><circle cx="5" cy="3" r="2.6" fill="#111"/><path d="M0 11a5 4.5 0 0 1 10 0z" fill="#111"/></svg>Register</div>
</header>

<nav class="abs nav">
  <div class="abs logo">Petal Sprite</div>
  <a style="left:387px">Home</a>
  <a style="left:498px">About</a>
  <a style="left:614px">Gallery</a>
  <a style="left:722px">Review</a>
  <a style="left:835px">Contact</a>
  <svg class="abs" style="left:894px;top:19px" width="12" height="12" viewBox="0 0 12 12"><circle cx="5" cy="5" r="3.6" stroke="#e4518b" stroke-width="1.5" fill="none"/><path d="M8 8l3 3" stroke="#e4518b" stroke-width="1.5"/></svg>
  <div class="abs login-btn">Log In</div>
</nav>

<section class="abs hero">
  <h1 class="abs">Fresh Flowers</h1>
  <h2 class="abs">Natural &amp; beautiful Flowers</h2>
  <p class="abs">Lorem ipsum dolor sit amet, consectetur adipiscing elit. Vitae platea suspendisse odio lectus vulputate. Nulla ornare morbi quis consequat dignissim enim ac, purus eros.</p>
  <div class="abs work-btn">Our Work</div>
  <div class="abs hero-visual" role="img" aria-label="Pink tulip bouquet with a gift box and paper hearts on a pink background"></div>
</section>

<section class="abs why">
  <div class="abs video" role="img" aria-label="Video still of a woman walking through a yellow flower field">
    <div class="abs bar"><i></i></div>
    <div class="abs ctrl"></div>
  </div>
  <h3 class="abs">Why <span>Choose Us</span></h3>
  <div class="abs copy">Lorem ipsum dolor sit amet, consectetur adipiscing elit. Vitae platea suspendisse odio lectus vulputate. Nulla ornare morbi quis consequat dignissim enim ac, purus eros pulvinar volutpat lobortis sed. Fames quis scelerisque netus et tristique nisi, commodo. Lorem ipsum dolor sit amet, consectetur adipiscing elit. Vitae platea suspendisse odio lectus vulputate. Nulla ornare morbi quis consequat dignissim enim ac<br><span style="display:block;height:10px"></span>Lorem ipsum dolor sit amet, consectetur adipiscing elit. Vitae platea suspendisse odio lectus vulputate. Nulla ornare morbi quis consequat dignissim enim ac</div>

  <div class="abs feature" style="left:5px">
    <svg width="36" height="38" viewBox="0 0 36 38" fill="none" stroke="#111" stroke-width="1.6"><path d="M18 36V16"/><circle cx="18" cy="10" r="6"/><path d="M18 26c-6 0-10-4-10-8 6 0 10 4 10 8zM18 24c6 0 10-4 10-8-6 0-10 4-10 8z"/></svg>
    <div><b>Custom Designs</b><small>For Every Event</small></div>
  </div>
  <div class="abs feature" style="left:240px">
    <svg width="40" height="36" viewBox="0 0 40 36" fill="none" stroke="#111" stroke-width="1.6"><rect x="4" y="6" width="32" height="26" rx="2"/><path d="M4 14h32M12 2v8M28 2v8"/><path d="M14 23l4 4 8-8"/></svg>
    <div><b>Event Styling</b><small>Weddings &amp; Hotels</small></div>
  </div>
  <div class="abs feature" style="left:476px">
    <svg width="32" height="40" viewBox="0 0 32 40" fill="none" stroke="#111" stroke-width="1.6"><path d="M8 18h16l-2 20H10z"/><path d="M16 18V8M16 10c-4-6-10-4-10 0 4 2 8 2 10 0zM16 10c4-6 10-4 10 0-4 2-8 2-10 0z"/></svg>
    <div><b>Seasonal Stems</b><small>Gentle &amp; Minimal</small></div>
  </div>
  <div class="abs feature" style="left:711px">
    <svg width="40" height="34" viewBox="0 0 40 34" fill="none" stroke="#111" stroke-width="1.6"><rect x="2" y="6" width="36" height="24" rx="2"/><path d="M2 8l18 12 18-12"/></svg>
    <div><b>Easy Booking</b><small>Reply Within 24h</small></div>
  </div>
</section>

<div class="abs band" style="left:130px;top:1035px;width:941px">Latest&nbsp;<span>Projects</span></div>

<div class="abs card" style="left:130px;top:1116px"><div class="abs tag">New</div><div class="abs pic" role="img" aria-label="Pink tulips in a white vase" style="background:linear-gradient(#f07aa3,#f5b4c9 60%,#f2f2f2)"></div><div class="abs name">Bridal Tulips</div><div class="abs event">Wedding <small>2024</small></div></div>
<div class="abs card" style="left:450px;top:1116px"><div class="abs tag">New</div><div class="abs pic" role="img" aria-label="Mixed red and yellow tulips in a lace wrapped pot" style="background:linear-gradient(#f08a2a,#e0452e 45%,#a6c46a)"></div><div class="abs name">Garden Party</div><div class="abs event">Celebration <small>2024</small></div></div>
<div class="abs card" style="left:768px;top:1116px"><div class="abs tag">New</div><div class="abs pic" role="img" aria-label="White tulips in a white vase" style="background:linear-gradient(#f3f3ea,#9cbf6c 55%,#f2f2f2)"></div><div class="abs name">White Calm</div><div class="abs event">Restaurant <small>2024</small></div></div>

<div class="abs card" style="left:130px;top:1442px"><div class="abs tag">New</div><div class="abs pic" role="img" aria-label="Red tulips in a white pot" style="background:linear-gradient(#d8242a,#6aa33e 55%,#eeeeee)"></div><div class="abs name">Hotel Lobby</div><div class="abs event">Hotel <small>2023</small></div></div>
<div class="abs card" style="left:450px;top:1442px"><div class="abs tag">New</div><div class="abs pic" role="img" aria-label="Red tulips in a textured white vase" style="background:linear-gradient(#c8262b,#e04c3c 45%,#ececec)"></div><div class="abs name">Salon Corner</div><div class="abs event">Beauty Salon <small>2023</small></div></div>
<div class="abs card" style="left:768px;top:1442px"><div class="abs tag">New</div><div class="abs pic" role="img" aria-label="Red and yellow tulips in a glass vase" style="background:linear-gradient(#f1a629,#d8402f 35%,#b7d69a)"></div><div class="abs name">Glass Vase</div><div class="abs event">Business <small>2023</small></div></div>

<div class="abs card" style="left:130px;top:1765px"><div class="abs tag">New</div><div class="abs pic" role="img" aria-label="Red tulips in a tall white vase" style="background:linear-gradient(#d02a2e,#5f9a3c 45%,#eef1f3)"></div><div class="abs name">Table Piece</div><div class="abs event">Wedding <small>2023</small></div></div>
<div class="abs card" style="left:450px;top:1765px"><div class="abs tag">New</div><div class="abs pic" role="img" aria-label="Multicolour tulips in a glass vase" style="background:linear-gradient(#f2b04d,#e36a5a 40%,#cfe3c4)"></div><div class="abs name">Spring Mix</div><div class="abs event">Birthday <small>2023</small></div></div>
<div class="abs card" style="left:768px;top:1765px"><div class="abs tag">New</div><div class="abs pic" role="img" aria-label="Red tulips in a terracotta pot" style="background:linear-gradient(#d21e26,#4f8c36 50%,#d4744c)"></div><div class="abs name">Terrace Pot</div><div class="abs event">Restaurant <small>2023</small></div></div>

<div class="abs band" style="left:134px;top:2074px;width:938px">Customer<span>’s Review</span></div>

<svg width="0" height="0" style="position:absolute"><defs><path id="st" d="M8 0l2.4 5.2 5.6.6-4.2 3.8 1.2 5.6L8 12.4 3 15.2l1.2-5.6L0 5.8l5.6-.6z"/></defs></svg>

<div class="abs review" style="left:143px">
  <svg class="abs stars" width="84" height="16" viewBox="0 0 84 16"><g fill="#e4518b"><use href="#st"/><use href="#st" x="17"/><use href="#st" x="34"/><use href="#st" x="51"/><use href="#st" x="68"/></g></svg>
  <p class="abs">Lorem ipsum dolor sit amet, consectetur adipiscing elit. Diam odio diam nullam elit. Sem cursus pellentesque proin at sit vitae. Suspendisse orci vestibulum, ac nisi, non viverra ultricies. Integer phasellus congue ridiculus posuere nunc sed cras.</p>
  <div class="abs avatar" role="img" aria-label="Client portrait" style="background:#c9a48d"></div>
  <div class="abs who"><b>Mira Holt</b><small>Happy Customer</small></div>
</div>
<div class="abs review" style="left:454px">
  <svg class="abs stars" width="84" height="16" viewBox="0 0 84 16"><g fill="#e4518b"><use href="#st"/><use href="#st" x="17"/><use href="#st" x="34"/><use href="#st" x="51"/><use href="#st" x="68"/></g></svg>
  <p class="abs">Lorem ipsum dolor sit amet, consectetur adipiscing elit. Diam odio diam nullam elit. Sem cursus pellentesque proin at sit vitae. Suspendisse orci vestibulum, ac nisi, non viverra ultricies. Integer phasellus congue ridiculus posuere nunc sed cras.</p>
  <div class="abs avatar" role="img" aria-label="Client portrait" style="background:#8f7a6d"></div>
  <div class="abs who"><b>Tomas Reed</b><small>Happy Customer</small></div>
</div>
<div class="abs review" style="left:766px">
  <svg class="abs stars" width="84" height="16" viewBox="0 0 84 16"><g fill="#e4518b"><use href="#st"/><use href="#st" x="17"/><use href="#st" x="34"/><use href="#st" x="51"/><use href="#st" x="68"/></g></svg>
  <p class="abs">Lorem ipsum dolor sit amet, consectetur adipiscing elit. Diam odio diam nullam elit. Sem cursus pellentesque proin at sit vitae. Suspendisse orci vestibulum, ac nisi, non viverra ultricies. Integer phasellus congue ridiculus posuere nunc sed cras.</p>
  <div class="abs avatar" role="img" aria-label="Client portrait" style="background:#7fb0c4"></div>
  <div class="abs who"><b>Ivo Lark</b><small>Happy Customer</small></div>
</div>

<div class="abs band" style="left:134px;top:2524px;width:938px">Contact&nbsp;<span>Us</span></div>

<section class="abs form">
  <div class="abs field" style="top:25px">Lena Vark</div>
  <div class="abs field" style="top:81px">lena.vark@mailbox.example</div>
  <div class="abs field" style="top:136px">+1 555 013 6620</div>
  <div class="abs field" style="top:191px;height:185px;padding-top:20px">Hello, I’m Lena Vark</div>
</section>
<div class="abs illus" role="img" aria-label="Illustration of a woman watering potted plants and flowers"></div>

<footer class="foot">
  <h4 class="abs" style="left:150px">Quick Link</h4>
  <a style="left:150px;top:3091px">Home</a>
  <a style="left:150px;top:3133px">About</a>
  <a style="left:150px;top:3174px">Gallery</a>
  <a style="left:150px;top:3216px">Review</a>
  <a style="left:150px;top:3258px">Contact</a>

  <h4 class="abs" style="left:387px">Extra Links</h4>
  <a style="left:387px;top:3091px">My Account</a>
  <a style="left:387px;top:3133px">My Events</a>
  <a style="left:387px;top:3174px">My Favorite</a>

  <h4 class="abs" style="left:654px">Locations</h4>
  <a style="left:654px;top:3091px">London</a>
  <a style="left:654px;top:3133px">USA</a>
  <a style="left:654px;top:3174px">France</a>

  <h4 class="abs" style="left:861px;top:3040px">Contact info</h4>
  <a style="left:861px;top:3091px">+1 555 018 4471</a>
  <a style="left:861px;top:3133px">hello@petalsprite.example</a>
  <a style="left:861px;top:3174px">12 Linden Lane, Brookfield</a>
</footer>

</body>
</html>
```